Re-design and craft the perfect CV platform

We are building a CV-based platform designed to connect employees and employers, with a strong focus on individual users. As we're just starting out, we're looking to have our platform and logo redesigned to better reflect our vision
https://app.lumoshire.com/
Colors like in the logo attached
#87C032 #6A6E71 #618930 - also you can add more colors if you like.
https://app.lumoshire.com/dashboard - This page would be nice if you plan it, like personal Bio dashboard. Attached picture (Dashboard wanted) one idea from how we would like to be, but we are open for new professional ideas/solutions.
https://app.lumoshire.com/posts - On this page we want to be showed the jobs posted. Attached one picture about our idea (jobs page wanted)
https://app.lumoshire.com/profile - design something nice.
Only Photoshop, Illustrator or Figma
Other pictures from the app attached (as looking right now)

Target Market(s)

Job seekers, HR, Recruiters

Industry/Entity Type

HR Tech

Number of Pages Required

5+ page

Colors
00AB8E
00BBA5
67D7C9
C6EFE9
E9F9F6

```html
<!DOCTYPE html>
<html lang="en">
<head>
<meta charset="utf-8">
<title>lumoshire – Profile Dashboard</title>
<link href="https://fonts.googleapis.com/css2?family=Figtree:wght@400;500;600;700&display=swap" rel="stylesheet">
<style>
:root{
  --teal:#00BBA5;
  --teal-dark:#00AB8E;
  --teal-light:#67D7C9;
  --mint:#C6EFE9;
  --mint-pale:#E9F9F6;
  --nav:#4a4e6d;
  --ink:#23252b;
  --muted:#8a8e96;
  --line:#e3e6ea;
  --blue:#1f5cf0;
  --bar:#0aa5c8;
  --page:#eef0f2;
}
*{box-sizing:border-box;margin:0;padding:0}
html,body{width:985px;height:1200px;overflow:hidden}
body{background:var(--page);font-family:"Figtree",sans-serif;color:var(--ink);position:relative}
.stage{position:absolute;left:0;top:301px;width:985px;height:597px;background:var(--teal)}
.app{position:absolute;left:28px;top:20px;width:936px;height:556px;background:#fff;border-radius:5px;overflow:hidden}
.topbar{position:absolute;left:0;top:0;width:100%;height:39px;background:var(--nav)}
.brand{position:absolute;left:43px;top:10px;font-size:15px;font-weight:700;color:var(--teal);display:flex;align-items:center;gap:5px}
.brand i{width:10px;height:10px;border-radius:50%;background:var(--teal);display:block}
.menu{position:absolute;left:242px;top:14px;display:flex;gap:17px;font-size:9px;font-weight:500;color:#fff}
.menu .off{color:#a4a7bb}
.tools{position:absolute;right:37px;top:9px;display:flex;gap:9px;align-items:center}
.tool{width:17px;height:17px;border:1px solid #7a7e98;border-radius:3px;display:flex;align-items:center;justify-content:center}
.me{width:18px;height:18px;border-radius:50%;background:linear-gradient(#e9c9b3,#9c7a66)}
.col{position:absolute;top:39px;bottom:0}
.col-left{left:0;width:217px}
.col-mid{left:217px;width:495px;border-left:1px solid var(--mint);border-right:1px solid var(--mint)}
.col-right{left:712px;width:224px}
.abs{position:absolute}
.portrait{left:54px;top:22px;width:109px;height:109px;border-radius:50%;border:4px solid var(--teal-light);background:linear-gradient(160deg,#d9d4ce,#8f7f74)}
.name{left:0;width:213px;top:140px;text-align:center;font-size:13px}
.updated{left:0;width:209px;top:158px;text-align:center;font-size:7.5px;color:var(--muted);line-height:9.5px}
.sec-title{font-size:11.5px;color:var(--teal);font-weight:500}
.about-h{left:41px;top:215px}
.about{left:41px;top:235px;width:146px;font-size:8.8px;line-height:12.3px}
.about-p{position:static}
.skills-h{left:41px;top:344px}
.chips{left:41px;top:360px;width:165px;display:flex;flex-wrap:wrap;gap:5px 4px}
.chip{border:1px solid var(--teal);color:var(--teal-dark);font-size:8px;border-radius:11px;height:21px;padding:0 10px;display:flex;align-items:center;white-space:nowrap}
.pen{font-size:9px;color:var(--muted);margin-left:5px}
.info-h{left:22px;top:24px}
.field{font-size:8.5px;color:var(--muted)}
.val{font-size:10px;color:var(--ink)}
.val a{color:var(--blue)}
.divider{left:0;right:0;top:153px;border-top:1px solid var(--mint)}
.block-h{font-size:11px;font-weight:500}
.viewall{font-size:8.5px;color:var(--teal-dark)}
.rule{border-top:1px solid var(--line)}
.jobs{display:flex;gap:7px}
.job{position:relative;width:106px;height:80px;border:1px solid var(--line);border-radius:4px;padding:13px 10px 0}
.job .co{font-size:14px;color:#4a3bb0;font-weight:500;line-height:15px}
.job .role{font-size:9px;font-weight:500;margin-top:5px;white-space:nowrap}
.job .org{font-size:7.8px;color:var(--muted);margin-top:2px}
.job .org b{color:var(--ink);font-weight:500}
.job .place{font-size:5.5px;color:var(--muted);margin-top:4px}
.job .place::before{content:"";display:inline-block;width:4px;height:4px;border-radius:50%;background:var(--teal);margin-right:4px}
.next{position:absolute;right:6px;top:32px;width:16px;height:16px;border-radius:50%;background:#8d9097;color:#fff;font-size:9px;display:flex;align-items:center;justify-content:center}
.status{left:24px;top:304px;width:332px;height:49px;border-radius:4px;background:linear-gradient(90deg,#0aa1c6,#00bba5);display:flex;align-items:center;padding-left:10px;color:#fff}
.status .pill{background:#fff;color:var(--teal-dark);font-size:7.5px;font-weight:500;border-radius:3px;height:23px;padding:0 8px;display:flex;align-items:center}
.num{font-size:25px;font-weight:500;margin-left:25px;line-height:1}
.lbl{font-size:9px;line-height:10.5px;margin-left:5px}
.num+.lbl+.num{margin-left:11px}
.company{width:99px;height:80px;border:1px solid var(--line);border-radius:4px;text-align:center;padding-top:10px}
.company .mk{width:24px;height:24px;margin:0 auto;border-radius:4px;background:#e5281c}
.company .cn{font-size:8px;margin-top:5px}
.company .rt{font-size:6px;color:var(--muted);margin-top:3px}
.company .rt b{color:var(--ink);font-weight:500}
.company .vj{font-size:6.5px;color:var(--blue);text-decoration:underline;margin-top:3px}
.tabs{left:19px;top:24px;display:flex;gap:35px;font-size:12px}
.tab-on{color:var(--teal-dark);font-weight:500;position:relative}
.tab-on::after{content:"";position:absolute;left:-6px;right:-16px;top:21px;height:2px;background:var(--teal-dark)}
.tab-off{color:var(--muted)}
.exp{left:24px;display:flex;gap:11px;align-items:center}
.exp .dot{width:32px;height:32px;border-radius:50%;background:var(--blue)}
.exp .t1{font-size:9.5px;font-weight:500}
.exp .t2{font-size:9px}
.exp .t3{font-size:7.5px}
.track{left:199px;top:80px;width:3px;height:276px;background:#e6ecf3;border-radius:2px}
.thumb{left:199px;top:80px;width:3px;height:52px;background:var(--bar);border-radius:2px}
.lang-h{left:24px;top:388px;font-size:11.5px;font-weight:500}
.lang-rule{left:18px;width:188px;top:409px}
.lang{left:24px;display:flex;align-items:center;font-size:10px;font-weight:500}
.lang span{width:47px}
.bar{width:99px;height:9px;border-radius:5px;background:#e6e9ec;overflow:hidden}
.bar i{display:block;height:100%;border-radius:5px;background:linear-gradient(90deg,var(--teal),var(--bar));color:#fff;font-style:normal;font-size:5.5px;padding-left:8px;line-height:9px}
</style>
</head>
<body>
<div class="stage">
  <div class="app">
    <header class="topbar">
      <div class="brand"><i></i>lumoshire</div>
      <nav class="menu"><span>Jobs</span><span>Companies</span><span class="off">CV</span></nav>
      <div class="tools">
        <div class="tool"><svg width="11" height="11" viewBox="0 0 24 24" fill="none" stroke="#fff" stroke-width="2"><circle cx="12" cy="12" r="3"/><circle cx="12" cy="12" r="8" stroke-dasharray="3 2"/></svg></div>
        <div class="tool"><svg width="10" height="11" viewBox="0 0 24 24" fill="none" stroke="#fff" stroke-width="2"><path d="M6 17V11a6 6 0 0 1 12 0v6l2 2H4z"/><path d="M10 21h4"/></svg></div>
        <div class="me" role="img" aria-label="User avatar photo"></div>
      </div>
    </header>

    <aside class="col col-left">
      <div class="abs portrait" role="img" aria-label="Profile photo of Mira T. Holden"></div>
      <div class="abs name">Mira T. Holden</div>
      <div class="abs updated">Profile last updated on<br>11/18/2024</div>
      <div class="abs about-h sec-title">About<span class="pen">✎</span></div>
      <div class="abs about"><p class="about-p">I am an organised, efficient and hard working person, and am willing to discover and accept new ideas which can be put into practice effectively. I am a good listener and learner, able to communicate well with a group and on an individual level.</p></div>
      <div class="abs skills-h sec-title">Skills</div>
      <div class="abs chips">
        <span class="chip">Markup</span><span class="chip">Styling</span><span class="chip">DOM Tools</span>
        <span class="chip">Grid Layout</span><span class="chip">Scripting</span>
        <span class="chip">SPA Design</span><span class="chip">Versioning</span>
      </div>
    </aside>

    <main class="col col-mid">
      <div class="abs info-h sec-title">Basic Information<span class="pen">✎</span></div>
      <div class="abs field" style="left:25px;top:47px">Age:</div>
      <div class="abs val" style="left:25px;top:62px">43 yrs</div>
      <div class="abs field" style="left:121px;top:47px">Sex:</div>
      <div class="abs val" style="left:121px;top:62px">Male</div>
      <div class="abs field" style="left:253px;top:47px">Qualification</div>
      <div class="abs val" style="left:253px;top:62px">CS Engineer</div>
      <div class="abs field" style="left:370px;top:47px">Driving Licesce</div>
      <div class="abs val" style="left:389px;top:62px">------</div>
      <div class="abs field" style="left:25px;top:94px">Location:</div>
      <div class="abs val" style="left:25px;top:109px">Romania</div>
      <div class="abs field" style="left:121px;top:94px">Email id</div>
      <div class="abs val" style="left:121px;top:109px"><a href="#">info@lumoshire.com</a></div>
      <div class="abs field" style="left:253px;top:94px">Mobile</div>
      <div class="abs val" style="left:253px;top:109px">+40-7215308462</div>
      <div class="abs field" style="left:370px;top:94px">Experience</div>
      <div class="abs val" style="left:370px;top:109px">10 Yrs</div>
      <div class="abs divider"></div>

      <div class="abs block-h" style="left:24px;top:180px">Recommended Jobs for you</div>
      <div class="abs viewall" style="left:322px;top:183px">view all</div>
      <div class="abs rule" style="left:24px;width:331px;top:199px"></div>
      <div class="abs jobs" style="left:24px;top:212px">
        <div class="job"><div class="co">Kestrel</div><div class="role">Lead - Retail Mall..</div><div class="org">Kestrel Group <b>★ 4.2</b></div><div class="place">Ahmedabad</div></div>
        <div class="job"><div class="co">Kestrel</div><div class="role">Head - Marketing..</div><div class="org">Leading Client <b>★ 4.2</b></div><div class="place">Ahmedabad</div></div>
        <div class="job"><div class="co">Kestrel</div><div class="role">Head - Marketing..</div><div class="org">Leading Client <b>★ 4.2</b></div><div class="place">Ahmedabad</div><span class="next">›</span></div>
      </div>

      <div class="abs status">
        <span class="pill">JOB APPLICATION STATUS</span>
        <span class="num">22</span><span class="lbl">Total<br>Applied</span>
        <span class="num">05</span><span class="lbl">Application<br>Updates</span>
      </div>

      <div class="abs block-h" style="left:24px;top:368px">Similar Jobs for you</div>
      <div class="abs viewall" style="left:322px;top:371px">view all</div>
      <div class="abs rule" style="left:24px;width:331px;top:387px"></div>
      <div class="abs jobs" style="left:24px;top:400px">
        <div class="job"><div class="co">Kestrel</div><div class="role">Lead - Retail Mall..</div><div class="org">Kestrel Group <b>★ 4.2</b></div><div class="place">Ahmedabad</div></div>
        <div class="job"><div class="co">Kestrel</div><div class="role">Head - Marketing..</div><div class="org">Leading Client <b>★ 4.2</b></div><div class="place">Ahmedabad</div></div>
        <div class="job"><div class="co">Kestrel</div><div class="role">Head - Marketing..</div><div class="org">Leading Client <b>★ 4.2</b></div><div class="place">Ahmedabad</div><span class="next">›</span></div>
      </div>

      <div class="abs block-h" style="left:370px;top:180px">Top Companies</div>
      <div class="abs company" style="left:371px;top:201px"><div class="mk"></div><div class="cn">Northwave</div><div class="rt"><b>★4.2</b> 1.3K reviews</div><div class="vj">view jobs</div></div>
      <div class="abs company" style="left:371px;top:288px"><div class="mk"></div><div class="cn">Northwave</div><div class="rt"><b>★4.2</b> 1.3K reviews</div><div class="vj">view jobs</div></div>
      <div class="abs company" style="left:371px;top:376px"><div class="mk"></div><div class="cn">Northwave</div><div class="rt"><b>★4.2</b> 1.3K reviews</div><div class="vj">view jobs</div></div>
      <div class="abs viewall" style="left:404px;top:467px;font-size:9px">view all</div>
    </main>

    <aside class="col col-right">
      <div class="abs tabs"><span class="tab-on">Experience</span><span class="tab-off">Education</span></div>
      <div class="abs track"></div><div class="abs thumb"></div>
      <div class="abs exp" style="top:62px"><span class="dot"></span><div><div class="t1">Orbis</div><div class="t2">Lead Front-end developer</div><div class="t3">Jan 2020- Present</div></div></div>
      <div class="abs exp" style="top:122px"><span class="dot"></span><div><div class="t1">Orbis</div><div class="t2">Lead Front-end developer</div><div class="t3">Jan 2020- Present</div></div></div>
      <div class="abs exp" style="top:181px"><span class="dot"></span><div><div class="t1">Orbis</div><div class="t2">Lead Front-end developer</div><div class="t3">Jan 2020- Present</div></div></div>
      <div class="abs exp" style="top:241px"><span class="dot"></span><div><div class="t1">Orbis</div><div class="t2">Lead Front-end developer</div><div class="t3">Jan 2020- Present</div></div></div>
      <div class="abs exp" style="top:300px"><span class="dot"></span><div><div class="t1">Orbis</div><div class="t2">Lead Front-end developer</div><div class="t3">Jan 2020- Present</div></div></div>
      <div class="abs lang-h">Languages</div>
      <div class="abs rule lang-rule"></div>
      <div class="abs lang" style="top:427px"><span>Roman</span><div class="bar"><i style="width:58%">65%</i></div></div>
      <div class="abs lang" style="top:454px"><span>Magyar</span><div class="bar"><i style="width:100%">100%</i></div></div>
      <div class="abs lang" style="top:481px"><span>Angol</span><div class="bar"><i style="width:73%">85%</i></div></div>
    </aside>
  </div>
</div>
</body>
</html>
```